New modern website for Kerbline Groundworks

Hi we are an existing company that has a current website http://www.kerblinegroundworks.co.nz/ we are looking to get a new vibrant looking website designed to take us further and gain more customers. We are after a simple easy to use website that does not confuse but we want to make an impact and stand out from the rest

Target Market(s)

Homeowners And Commercial Businesses

Industry/Entity Type

It Company

Coding

Coded - Design and coding required

Number of Pages Required

2 page

```html
<!DOCTYPE html>
<html lang="en">
<head>
<meta charset="utf-8">
<title>Kerbline Groundworks</title>
<link href="https://fonts.googleapis.com/css2?family=PT+Sans:wght@400;700&family=Open+Sans:wght@400;600;700&display=swap" rel="stylesheet">
<style>
:root{
  --dark:#3a3a3a;
  --card:#454545;
  --ink:#3c4148;
  --footer:#3c4149;
  --muted:#9a9a9a;
  --light:#f2f2f2;
  --white:#ffffff;
  --accent:#3aa27a;
  --asphalt1:#2b2b2b;
  --asphalt2:#4a4a4a;
}
*{box-sizing:border-box;margin:0;padding:0}
html,body{width:1200px;height:2889px;overflow:hidden}
body{position:relative;background:var(--white);font-family:"Open Sans",Arial,sans-serif;color:var(--ink)}
.abs{position:absolute}
.topbar{left:0;top:0;width:1200px;height:27px;background:var(--dark);color:var(--white);font-size:11px;font-weight:600}
.topbar .welcome{left:14px;top:6px}
.topbar .contact{right:80px;top:6px;display:flex;gap:24px;align-items:center}
.topbar .contact span{display:flex;align-items:center;gap:6px}
.header{left:0;top:27px;width:1200px;height:106px;background:var(--white)}
.brand{left:58px;top:26px;display:flex;align-items:center;gap:12px;font-family:"PT Sans",sans-serif;font-weight:700;font-size:28px;color:var(--dark)}
.brand .mark{width:20px;height:20px;background:var(--dark)}
.nav{left:545px;top:0;display:flex;height:79px}
.nav a{display:flex;align-items:center;justify-content:center;font-size:11px;font-weight:700;color:var(--dark);text-decoration:none;width:103px;position:relative}
.nav a.active{background:var(--dark);color:var(--white);width:81px;margin-right:10px}
.nav a.drop::after{content:"";position:absolute;bottom:24px;left:50%;margin-left:-3px;border:3px solid transparent;border-top-color:var(--dark)}
.hero{left:0;top:133px;width:1200px;height:533px;background:radial-gradient(ellipse at 50% 40%,var(--asphalt2),var(--asphalt1))}
.hero h1{position:absolute;top:184px;width:100%;text-align:center;color:var(--white);font-family:"PT Sans",sans-serif;font-weight:700;font-size:62px;letter-spacing:1px;line-height:1}
.hero h2{position:absolute;top:250px;width:100%;text-align:center;color:var(--white);font-family:"PT Sans",sans-serif;font-weight:700;font-size:38px;line-height:1}
.arrow{top:267px;width:52px;height:54px;background:var(--white);display:flex;align-items:center;justify-content:center}
.cards{left:52px;top:566px;display:flex;gap:27px}
.card{width:347px}
.card .body{background:var(--card);color:var(--white);height:199px;padding:26px 30px}
.card h3{font-family:"PT Sans",sans-serif;font-size:22px;font-weight:700;margin-bottom:14px}
.card p{font-size:11.5px;line-height:19px}
.card .pic{height:196px}
.welcome{left:0;top:961px;width:1200px;height:647px;background:var(--light)}
.welcome h2{position:absolute;top:62px;width:100%;text-align:center;font-family:"PT Sans",sans-serif;font-size:38px;font-weight:700;color:var(--ink)}
.welcome .sub{position:absolute;top:102px;width:100%;text-align:center;font-family:"PT Sans",sans-serif;font-size:23px;font-weight:700;color:#5d6570;letter-spacing:.5px}
.feature{top:173px;width:270px;text-align:center}
.feature .icon{width:124px;height:124px;border-radius:50%;background:var(--ink);margin:0 auto;display:flex;align-items:center;justify-content:center}
.feature h4{margin-top:42px;font-family:"PT Sans",sans-serif;font-size:22px;font-weight:700;line-height:24px;color:var(--ink)}
.feature p{margin-top:14px;font-size:11px;line-height:21px;color:var(--muted)}
.projects{left:0;top:1608px;width:1200px;height:565px}
.projects h2{position:absolute;left:52px;top:58px;font-family:"PT Sans",sans-serif;font-size:22px;font-weight:700;color:var(--dark)}
.project{top:112px;width:350px}
.project .pic{height:225px}
.project h5{margin-top:24px;font-size:12px;font-weight:700;color:#111}
.project p{margin-top:4px;font-size:11px;line-height:15px;color:#333}
.btn{display:inline-block;margin-top:24px;background:#222;color:var(--white);font-size:10px;font-weight:700;padding:8px 20px;border-radius:3px}
.services{left:0;top:2173px;width:1200px;height:408px;background:var(--light)}
.col{top:44px;width:252px}
.col .num{font-family:"PT Sans",sans-serif;font-size:44px;font-weight:700;color:var(--ink);line-height:1}
.col h4{margin-top:20px;font-family:"PT Sans",sans-serif;font-size:22px;font-weight:700;color:var(--ink)}
.col hr{margin-top:16px;border:0;border-top:1px dotted #aaa}
.col ul{list-style:none;margin-top:28px}
.col li{font-size:12px;line-height:24.5px;color:#8a8a8a}
.col li::before{content:"→";color:var(--accent);margin-right:9px;font-size:11px}
.col .more{margin-top:18px;display:flex;align-items:center;gap:8px;font-size:15px;font-weight:700;color:var(--dark)}
.col .more i{width:14px;height:14px;border-radius:50%;background:var(--dark);display:inline-block}
.footer{left:0;top:2581px;width:1200px;height:308px;background:var(--footer);color:var(--white);text-align:center}
.social{position:absolute;top:60px;width:100%;display:flex;justify-content:center;gap:14px}
.social i{width:16px;height:16px;border-radius:50%;background:var(--white);display:block}
.footer .copy{position:absolute;top:84px;width:100%;font-family:"PT Sans",sans-serif;font-size:42px;font-weight:700}
.footer .legal{position:absolute;top:153px;width:100%;font-size:12px;font-weight:700}
.footer .legal small{font-size:10px}
.totop{left:579px;top:206px;width:42px;height:42px;border-radius:50%;background:#d9d9d9;display:flex;align-items:center;justify-content:center}
</style>
</head>
<body>
<div class="abs topbar">
  <span class="abs welcome">Welcome to Kerbline Groundworks</span>
  <div class="abs contact">
    <span><svg width="10" height="10" viewBox="0 0 10 10"><path d="M2 1l2 2-1 1.5c.6 1.2 1.3 1.9 2.5 2.5L7 6l2 2-1.5 1.5C4.5 9 1 5.5.5 2.5z" fill="#fff"/></svg>09 555 0142</span>
    <span><svg width="11" height="9" viewBox="0 0 11 9"><rect x=".5" y=".5" width="10" height="8" fill="none" stroke="#fff"/><path d="M.5.5l5 4.5 5-4.5" fill="none" stroke="#fff"/></svg>info@kerblinegroundworks.co.nz</span>
  </div>
</div>

<header class="abs header">
  <div class="abs brand"><span class="mark"></span>Kerbline Groundworks</div>
  <nav class="abs nav">
    <a class="active">HOME</a>
    <a class="drop">ABOUT</a>
    <a class="drop">SERVICES</a>
    <a>PROJECTS</a>
    <a>BLOG</a>
    <a>CONTACTS</a>
  </nav>
</header>

<section class="abs hero" role="img" aria-label="Close-up photo of fresh asphalt surface">
  <h1>SETTING THE STANDARDS FOR</h1>
  <h2>CONCRETE &amp; ASPHALTERS</h2>
  <div class="abs arrow" style="left:0"><svg width="14" height="20" viewBox="0 0 14 20"><path d="M11 2L3 10l8 8" fill="none" stroke="#333" stroke-width="3"/></svg></div>
  <div class="abs arrow" style="right:0"><svg width="14" height="20" viewBox="0 0 14 20"><path d="M3 2l8 8-8 8" fill="none" stroke="#333" stroke-width="3"/></svg></div>
</section>

<div class="abs cards">
  <article class="card">
    <div class="body"><h3>OUR EXPERTISE</h3><p>We have a reputation with clients in and around Auckland for achieving great results on time and within budget every time. We are proud to share our years of experience.</p></div>
    <div class="pic" role="img" aria-label="Gold laurel anniversary emblem with the number 70" style="background:radial-gradient(circle,#f3d44a,#fff 70%)"></div>
  </article>
  <article class="card">
    <div class="body"><h3>CONCRETING &amp; ASPHALT</h3><p>When it comes to all asphalt services, you can rest assured we will work around your schedule, requirements and budget. Servicing throughout Auckland, we specialise in.</p></div>
    <div class="pic" role="img" aria-label="Photo of a straight paved road through green fields under blue sky" style="background:linear-gradient(#3f87d8,#a9cdeb 45%,#5f8a3a 55%,#555 100%)"></div>
  </article>
  <article class="card">
    <div class="body"><h3>ADDITIONAL SERVICES</h3><p>As part of our asphalt services, we are proud to offer a range of related services to our clients in the eastern suburbs and greater Auckland. Specialising in residential, commercial and industrial projects.</p></div>
    <div class="pic" role="img" aria-label="Photo of workers laying concrete beside a concrete mixer truck" style="background:linear-gradient(#c9ccd0,#8e8f8f 60%,#777)"></div>
  </article>
</div>

<section class="abs welcome">
  <h2>WELCOME!</h2>
  <p class="sub">Complete asphalt services for your next project in Auckland</p>
  <div class="abs feature" style="left:44px">
    <div class="icon"><svg width="60" height="50" viewBox="0 0 60 50"><path d="M8 44c20-6 10-22 40-32" fill="none" stroke="#fff" stroke-width="10" stroke-linecap="round"/><path d="M10 42c20-6 10-22 38-30" fill="none" stroke="#3c4148" stroke-width="1.5" stroke-dasharray="4 4"/></svg></div>
    <h4>Complete<br>asphalt services</h4>
    <p>As your local one-stop shop you will receive durable solutions by calling on Kerbline Groundworks for all asphalt services. Arriving at your property in Auckland at an agreed upon time,we promise to leave no mess behind, only quality results. So please feel free to call us todayto discuss what we can do for your project.</p>
  </div>
  <div class="abs feature" style="left:323px">
    <div class="icon"><svg width="66" height="44" viewBox="0 0 66 44"><rect x="2" y="18" width="14" height="16" fill="#fff"/><ellipse cx="38" cy="18" rx="22" ry="13" fill="#fff"/><rect x="2" y="32" width="62" height="4" fill="#fff"/><circle cx="14" cy="38" r="5" fill="#fff" stroke="#3c4148" stroke-width="2"/><circle cx="50" cy="38" r="5" fill="#fff" stroke="#3c4148" stroke-width="2"/></svg></div>
    <h4>Asphalt<br>concreting work</h4>
    <p>When it comes to all asphalt services, you can rest assured we will work around your schedulerequirements and budget. Servicing throughout Auckland, we specialise in completing a wide range of asphalt and concreting projects including:</p>
  </div>
  <div class="abs feature" style="left:605px">
    <div class="icon"><svg width="56" height="64" viewBox="0 0 56 64"><path d="M16 22a12 10 0 0 1 24 0z" fill="#fff"/><rect x="14" y="22" width="28" height="4" fill="#fff"/><rect x="18" y="30" width="20" height="14" rx="6" fill="#fff"/><path d="M10 62c0-12 8-16 18-16s18 4 18 16z" fill="#fff"/><path d="M6 8v40" stroke="#fff" stroke-width="3"/><path d="M2 4h8v8H2z" fill="#fff"/></svg></div>
    <h4>All<br>labour</h4>
    <p>Guiding you throughout the process of our asphalt services, you can count on our team inAuckland to provide all labour for your specific needs</p>
  </div>
  <div class="abs feature" style="left:886px">
    <div class="icon"><svg width="50" height="60" viewBox="0 0 50 60"><path d="M25 4C25 4 12 22 12 32a13 13 0 0 0 26 0C38 22 25 4 25 4z" fill="#fff"/><path d="M4 46c6 8 36 8 42 0" fill="none" stroke="#fff" stroke-width="3"/></svg></div>
    <h4>Additional<br>services</h4>
    <p>As part of our asphalt services, we are proud to offer a range of related services to our clientsin the eastern suburbs and greater Auckland. Specialising in residential, commercial andindustrial projects, including hospitals and factories, we can provide expertise for:</p>
  </div>
</section>

<section class="abs projects">
  <h2>LAST PROJECTS</h2>
  <article class="abs project" style="left:52px">
    <div class="pic" role="img" aria-label="Photo of a new asphalt driveway beside a house and garden" style="background:linear-gradient(#b9cde0,#6d7f5a 45%,#3e3e3e 75%)"></div>
    <h5>LOREM IPSUM DOLOR SIT AMET</h5>
    <p>Aliquam dapibus tincidunt metus. Praesent justo dolor, lobortis quis, lobortis dignissim, pulvinar ac, lorem. Lorem ipsum dolor sit amet, consectetuer adipiscing elit. Praesent...</p>
    <span class="btn">MORE</span>
  </article>
  <article class="abs project" style="left:425px">
    <div class="pic" role="img" aria-label="Photo of a narrow asphalt driveway between wooden fences" style="background:linear-gradient(90deg,#a8876a,#2a2f3a 40%,#2a2f3a 60%,#6e6e6e)"></div>
    <h5>BLANDITIIS PRAESENTIUM</h5>
    <p>Aliquam dapibus tincidunt metus. Praesent justo dolor, lobortis quis, lobortis dignissim, pulvinar ac, lorem. Lorem ipsum dolor sit amet, consectetuer adipiscing elit. Praesent...</p>
    <span class="btn">MORE</span>
  </article>
  <article class="abs project" style="left:798px">
    <div class="pic" role="img" aria-label="Photo of a wide asphalt parking area surrounded by trees" style="background:linear-gradient(#3d4f35,#55604a 35%,#4b4b4b 60%,#3a3a3a)"></div>
    <h5>ELIGENDI OPTIO</h5>
    <p>Aliquam dapibus tincidunt metus. Praesent justo dolor, lobortis quis, lobortis dignissim, pulvinar ac, lorem. Lorem ipsum dolor sit amet, consectetuer adipiscing elit. Praesent...</p>
    <span class="btn">MORE</span>
  </article>
</section>

<section class="abs services">
  <div class="abs col" style="left:52px">
    <div class="num">01.</div><h4>ASPHALT</h4><hr>
    <ul><li>Car parks</li><li>Driveway construction</li><li>Chip sealing</li><li>Metal prep, loose chips and repairs</li></ul>
    <div class="more"><i></i>more</div>
  </div>
  <div class="abs col" style="left:333px">
    <div class="num">02.</div><h4>CONCRETING WORK</h4><hr>
    <ul><li>Kerbing and asphalt</li><li>Retaining walls</li><li>Sports courts</li><li>Hard landscaping</li></ul>
    <div class="more"><i></i>more</div>
  </div>
  <div class="abs col" style="left:614px">
    <div class="num">03.</div><h4>ALL LABOUR</h4><hr>
    <ul><li>Digging</li><li>Construction</li><li>Road marking</li><li>Resurfacing, sealing</li><li>Design Maintenance, repairs</li><li>Sawing</li></ul>
    <div class="more"><i></i>more</div>
  </div>
  <div class="abs col" style="left:895px">
    <div class="num">04.</div><h4>ADDITIONAL SERVICES</h4><hr>
    <ul><li>Concrete laying</li><li>Footings</li><li>Excavation</li><li>Site work services</li></ul>
    <div class="more"><i></i>more</div>
  </div>
</section>

<footer class="abs footer">
  <div class="social"><i></i><i></i><i></i><i></i><i></i></div>
  <div class="copy">copyright</div>
  <div class="legal">Kerbline Groundworks <small>© 2016</small> Privacy Policy</div>
  <div class="abs totop"><svg width="16" height="10" viewBox="0 0 16 10"><path d="M2 8l6-6 6 6" fill="none" stroke="#3c4149" stroke-width="2.5"/></svg></div>
</footer>
</body>
</html>
```